Logo-Design für Restaurant Morgentau
Sehr zufrieden, immer hilfsbereit, Passende Antwort für jeder Frage, sehr reibungslos schnell dolles Entwurf erfasst was richtig der Inhalt passt. Ist wirklich nur zum empfehlen. Vielen Verdienten Dank Mit freundlichen Grüßen Lutfi
Zielgruppe
Deutsches Restaurant, Bürgerliche Küche
Aufgabenstellung
inklusive flyer Design .
Folgender Inhalt sollte auf dem Flyer vertreten:
vorder und rückseite in format von 10,5x 21cm quer
Neueröffnung am 01.07.2016
Täglisch Mittagskarte ab 6,90 Euro
Ab 17:00 Uhr Staek , Schnitzel , Flammkuchen , Salate und andere Leckereien von MORGENTAU
Öffnungzeiten Mo- Samstag 11:30- 14:30 und 17:00- 23:00
Sonntag 10:00- 14:00 Brunch (Der erste brunch findet am 17.07.2016)
eine Reserviereung wird Empfohlen, da nur eine begrenzte Anzahl von Plätzen zur Verfügeung steht.
Alle Gerichte auch zum Mitnehmen!
Reserverung unter 06152 / 84 36 927, Gerne richten wir auch Ihre private Veranstaltung aus

```html
<!DOCTYPE html>
<html lang="de">
<head>
<meta charset="utf-8">
<title>Restaurant Morgentau – Geschäftsausstattung</title>
<link href="https://fonts.googleapis.com/css2?family=Arimo:wght@400;700&family=Playfair+Display:wght@700&display=swap" rel="stylesheet">
<style>
  :root {
    --ink: #0b0b0b;
    --paper: #ffffff;
    --board: #ffffff;
    --nav-bg: #f1f1f1;
    --muted: #555555;
    --rule: #111111;
    --band-top: #2a2a2a;
    --gold: #c9973f;
    --panel-dark: #141414;
    --card-stage-light: #e9e9e9;
    --card-stage-dark: #1a1a1a;
    --watermark: rgba(0,0,0,0.13);
  }
  * { box-sizing: border-box; margin: 0; padding: 0; }
  html, body { width: 1200px; height: 1200px; overflow: hidden; background: var(--board); }
  body { position: relative; font-family: "Arimo", Arial, sans-serif; color: var(--ink); }

  .sheet { position: absolute; background: var(--paper); box-shadow: 4px 6px 14px rgba(0,0,0,0.35); overflow: hidden; }
  .abs { position: absolute; }

  /* brand wordmark */
  .wordmark { font-family: "Arimo", Arial, sans-serif; font-weight: 700; white-space: nowrap; line-height: 1; }
  .wordmark-dot { display: inline-block; border-radius: 50%; vertical-align: middle; }

  /* website */
  .website { left: 13px; top: 11px; width: 488px; height: 690px; }
  .site-logo { left: 33px; top: 28px; font-size: 19px; }
  .social { left: 329px; top: 24px; display: flex; gap: 8px; }
  .social span { width: 32px; height: 32px; border-radius: 50%; background: var(--ink); display: block; }
  .site-rule { left: 30px; top: 63px; width: 428px; height: 1.5px; background: var(--rule); }
  .nav { left: 30px; top: 104px; width: 428px; height: 12px; background: var(--nav-bg); font-size: 10px; }
  .nav a { position: absolute; top: 0; line-height: 12px; color: var(--ink); text-decoration: none; }
  .nav a.current { background: var(--ink); color: var(--paper); width: 47px; text-align: center; }
  .hero { left: 30px; top: 132px; width: 431px; height: 244px; background: var(--ink); display: flex; flex-direction: column; align-items: center; justify-content: center; color: var(--paper); }
  .hero .wordmark { font-size: 46px; }
  .hero .sub { font-family: "Playfair Display", Georgia, serif; font-size: 13px; letter-spacing: 2px; margin-top: 6px; }
  .tabs { top: 400px; font-size: 14px; }
  .tab-rule { left: 30px; top: 432px; width: 423px; height: 2px; background: var(--rule); }
  .teaser-title { font-size: 22px; color: #222; }
  .photo { height: 91px; }
  .photo-stones { left: 30px; top: 484px; width: 165px; background: linear-gradient(180deg, #c9c2b5 0%, #ddd2c0 45%, #9c9488 100%); }
  .photo-pool { left: 287px; top: 484px; width: 171px; background: linear-gradient(180deg, #3c3f3e 0%, #8fa0b4 40%, #2b3750 75%, #1b2130 100%); }
  .teaser-head { font-weight: 700; font-size: 10.6px; line-height: 14.5px; width: 175px; }
  .teaser-text { font-size: 7.8px; color: #444; }
  .site-footer { left: 0; top: 655px; width: 488px; height: 35px; background: var(--ink); border-top: 4px solid var(--band-top); color: var(--paper); font-size: 14px; text-align: right; padding: 8px 19px 0 0; }

  /* letterhead */
  .letter { left: 516px; top: 11px; width: 487px; height: 688px; }
  .letter-logo { left: 0; top: 30px; width: 100%; text-align: center; font-size: 21px; }
  .letter-logo .sub { display: block; font-family: "Playfair Display", Georgia, serif; font-size: 6px; letter-spacing: 1.5px; margin-top: 2px; }
  .small { font-size: 6.2px; line-height: 7.6px; }
  .sender { left: 71px; top: 93px; }
  .recipient { left: 71px; top: 104px; }
  .letter-body { left: 71px; top: 218px; width: 350px; font-size: 6.7px; line-height: 10.6px; }
  .letter-body p { margin-bottom: 10.6px; }
  .watermark { left: 120px; top: 308px; font-size: 48px; color: var(--watermark); }
  .signature { left: 70px; top: 537px; font-size: 8px; line-height: 9.6px; }
  .letter-foot { top: 639px; font-size: 6px; line-height: 7.6px; color: #222; }
  .letter-foot .label { color: #888; }
  .letter-band { left: 0; top: 677px; width: 100%; height: 11px; background: var(--ink); }

  /* business cards */
  .card-stage { width: 334px; height: 209px; display: flex; align-items: center; justify-content: center; }
  .stage-light { left: 49px; top: 735px; background: var(--card-stage-light); }
  .stage-dark { left: 49px; top: 957px; background: var(--card-stage-dark); }
  .card { position: relative; width: 236px; height: 138px; background: var(--paper); box-shadow: 0 3px 8px rgba(0,0,0,0.3); }
  .card .wordmark { font-size: 15px; }
  .card-title { font-size: 8px; letter-spacing: 1px; }
  .card-band { left: 0; top: 20px; width: 100%; height: 20px; background: var(--ink); color: var(--paper); font-weight: 700; padding: 6px 0 0 34px; }
  .tiny { font-size: 5.4px; line-height: 7px; }

  /* gold panel */
  .gold-panel { left: 405px; top: 709px; width: 795px; height: 491px; background: radial-gradient(ellipse at 50% 50%, #232323 0%, var(--panel-dark) 70%); display: flex; flex-direction: column; align-items: center; justify-content: center; color: var(--gold); padding-bottom: 10px; }
  .gold-panel .wordmark { font-size: 112px; letter-spacing: -2px; }
  .gold-panel .sub { font-family: "Playfair Display", Georgia, serif; font-size: 24px; letter-spacing: 5px; margin-top: 16px; }
</style>
</head>
<body>

<!-- website -->
<section class="sheet website" aria-label="Website">
  <div class="abs site-logo wordmark">Morgentau</div>
  <div class="abs social" aria-label="Soziale Netzwerke"><span></span><span></span><span></span></div>
  <div class="abs site-rule"></div>
  <nav class="abs nav">
    <a class="current" style="left:17px">Home</a>
    <a style="left:86px">About us</a>
    <a style="left:156px">Service</a>
    <a style="left:214px">Blog</a>
    <a style="left:261px">Contact</a>
  </nav>
  <div class="abs hero">
    <div class="wordmark">Morgentau</div>
    <div class="sub">RESTAURANT</div>
  </div>
  <div class="abs tabs" style="left:47px">Text Text</div>
  <div class="abs tabs" style="left:207px">Text Text</div>
  <div class="abs tabs" style="left:366px">Text Text</div>
  <div class="abs tab-rule"></div>
  <div class="abs teaser-title" style="left:58px; top:448px">Text Text</div>
  <div class="abs teaser-title" style="left:326px; top:455px">Text Text</div>
  <div class="abs photo photo-stones" role="img" aria-label="Foto: gestapelte Steine am Strand bei Sonnenuntergang"></div>
  <div class="abs photo photo-pool" role="img" aria-label="Foto: Person in Yogapose am Infinity-Pool vor Bergkulisse"></div>
  <div class="abs teaser-head" style="left:30px; top:585px">Commodo aliquip eu occaecat et ut nulla veniam cillum</div>
  <div class="abs teaser-head" style="left:287px; top:585px">Commodo aliquip eu occaecat et ut nulla veniam cillum</div>
  <div class="abs teaser-text" style="left:30px; top:623px">Minim aliqua est fugiat sint. Excepteur ipsum</div>
  <div class="abs teaser-text" style="left:287px; top:623px">Minim aliqua est fugiat sint. Excepteur ipsum</div>
  <footer class="abs site-footer">Text Text text</footer>
</section>

<!-- letterhead -->
<section class="sheet letter" aria-label="Briefbogen">
  <div class="abs letter-logo"><span class="wordmark">Morgentau</span><span class="sub">RESTAURANT</span></div>
  <div class="abs sender small">Name • Adresse 1 • Adresse 2</div>
  <div class="abs recipient small">Max Mustermann<br>Straße<br>Ort</div>
  <div class="abs watermark wordmark">Morgentau</div>
  <div class="abs letter-body">
    <p>Sehr geehrter Herr,</p>
    <p>Esse ut ex. Sed esse mollit quis laboris in pariatur, anim ut aliquip ullamco voluptate. Ex consectetur culpa in eu, proident aliqua mollit sint reprehenderit?</p>
    <p>Incididunt ut in dolore reprehenderit aliqua ad, mollit anim fugiat ea. Enim consequat ad, ipsum ad sint culpa amet consectetur, sed cupidatat. Sit commodo ut. Non, nisi excepteur, fugiat voluptate ullamco eu labore: Pariatur sint laboris. Ipsum ea culpa qui nisi id exercitation, voluptate sit qui esse. Nisi, sunt ipsum occaecat commodo ut, magna veniam sed sit. Nisi officia minim reprehenderit dolore exercitation in fugiat, pariatur do reprehenderit dolore? Dolore, nostrud dolor velit.</p>
    <p>Aute aliqua, sed nostrud ut in ex nulla id ut non mollit aute voluptate. Occaecat anim ea nostrud et dolor est fugiat tempor excepteur. Amet, esse culpa commodo proident ut commodo do aute.<br>Qui sed adipisicing voluptate est. Fugiat sint veniam in duis non deserunt sint commodo: Occaecat dolore magna ea mollit, enim dolor exercitation dolore sunt magna aute lorem ea ad exercitation?</p>
    <p>Consectetur id ea proident. Dolore sunt velit et reprehenderit aliqua eiusmod. Exercitation eu laboris ex occaecat deserunt dolore et excepteur sint in dolore nostrud laboris dolore culpa quis cupidatat. Ea cillum et. In, consectetur amet.</p>
    <p>In elit ullamco culpa, enim reprehenderit est dolore magna, ad lorem. Ipsum ea, minim mollit sit minim. Sed voluptate velit dolor in magna non aliqua cillum in officia in excepteur. Officia veniam ut, pariatur ad veniam reprehenderit ex sint consequat magna. Amet sunt, duis velit do qui culpa, adipisicing sint mollit officia in culpa aliqua. Lorem, aliqua non labore est enim. Ad officia commodo do eu consequat. Sunt in, eu cupidatat, qui aute proident, adipisicing fugiat dolore velit ut in sint eiusmod commodo laboris do.</p>
    <p style="margin-top:16px">Mit freundlichen Grüßen</p>
  </div>
  <div class="abs signature">Name<br>Geschäftsführer</div>
  <div class="abs letter-foot" style="left:71px">Name<br>Adresse 1<br>Adresse 2</div>
  <div class="abs letter-foot" style="left:209px"><span class="label">Tel.:</span> +49 (0) 123456<br><span class="label">Fax.:</span> +49 (0) 123456<br><span class="label">E-mail:</span> info@postkorb.de</div>
  <div class="abs letter-foot" style="left:360px">Bankverbindung: xxxxxxxxxx<br>IBAN: xxxxxxxxxxxxxx<br>BIC: xxxxxxxxxxxxxxxxx</div>
  <div class="abs letter-band"></div>
</section>

<!-- business card front -->
<section class="abs card-stage stage-light" aria-label="Visitenkarte Vorderseite">
  <div class="card">
    <div class="abs wordmark" style="left:20px; top:16px">Morgentau</div>
    <div class="abs card-title" style="left:20px; top:46px">MORGENTAU RESTAURANT</div>
    <div class="abs tiny" style="left:20px; top:98px">Adresse 1<br>Adresse 2</div>
    <div class="abs tiny" style="left:92px; top:91px"><b>tel:</b> 01234 000000<br><b>fax:</b> 01234 000000<br><b>mobile:</b> 01234 000000</div>
    <div class="abs tiny" style="left:160px; top:91px"><b>email:</b> kontakt@postkorb.de<br><b>website:</b> www.morgentau-kueche.de</div>
    <div class="abs" style="left:0; bottom:0; width:100%; height:5px; background:var(--ink)"></div>
  </div>
</section>

<!-- business card back -->
<section class="abs card-stage stage-dark" aria-label="Visitenkarte Rückseite">
  <div class="card">
    <div class="abs card-band card-title">MORGENTAU RESTAURANT</div>
    <div class="abs tiny" style="left:150px; top:50px"><b>E:</b> kontakt@postkorb.de<br><b>W:</b> www.morgentau-kueche.de</div>
    <div class="abs tiny" style="left:150px; top:70px"><b>T:</b> 01234 000000<br><b>F:</b> 01234 000000</div>
    <div class="abs tiny" style="left:20px; top:88px">Adresse 1<br>Adresse 2</div>
    <div class="abs wordmark" style="left:20px; top:112px; font-size:11px">Morgentau</div>
  </div>
</section>

<!-- gold logo -->
<section class="abs gold-panel" aria-label="Logo in Gold">
  <div class="wordmark">Morgentau</div>
  <div class="sub">RESTAURANT</div>
</section>

</body>
</html>
```